Business Card Design Project

I have just chosen a logo and would now like this designed onto a business card for my hair salon. I would like it to be classy not to busy and have a wow factor when people look at them
Has to Include on card:
Logo Design
And business details below
Kellie-ann Drummond (owner)
0482 736 219
Rdw@vomblet.com.au
71 Willowmere Rise Corvin Cove
Logo is now attached please provide designs
Hair

```html
<!DOCTYPE html>
<html lang="en">
<head>
<meta charset="utf-8">
<title>Kellie-ann Drummond Salon – Business Card</title>
<link rel="stylesheet" href="https://fonts.googleapis.com/css2?family=Quicksand:wght@400;500&display=swap">
<style>
  :root {
    --stage: #e6e6e6;
    --card-dark-centre: #3b3b3b;
    --card-dark-edge: #1d1d1d;
    --card-light: #ffffff;
    --frame-blue: #3d8fd6;
    --cyan: #27b4d3;
    --magenta: #ec1e8c;
    --ink: #1a1a1a;
    --muted: #4a4a4a;
    --wordmark: #d9d9d9;
    --wash: #bfe8ef;
  }
  * { box-sizing: border-box; margin: 0; padding: 0; }
  html, body {
    width: 1200px;
    height: 1200px;
    overflow: hidden;
    background: var(--stage);
    font-family: "Quicksand", sans-serif;
  }
  .canvas {
    position: relative;
    width: 1200px;
    height: 1200px;
  }
  .card {
    position: absolute;
    left: 190px;
    width: 820px;
    height: 501px;
    box-shadow: 0 6px 18px rgba(0, 0, 0, 0.18);
    overflow: hidden;
  }

  /* Back of card */
  .card--back {
    top: 70px;
    background: radial-gradient(ellipse at 50% 45%, var(--card-dark-centre) 0%, var(--card-dark-edge) 75%);
    display: flex;
    flex-direction: column;
    align-items: center;
    justify-content: center;
    gap: 34px;
  }
  .wordmark__square {
    width: 170px;
    height: 170px;
    background: var(--magenta);
  }
  .wordmark__name {
    color: var(--wordmark);
    font-weight: 400;
    font-size: 34px;
    letter-spacing: 3px;
    text-transform: uppercase;
  }

  /* Front of card */
  .card--front {
    top: 629px;
    background: var(--card-light);
  }
  .card__frame {
    position: absolute;
    inset: 20px;
    border: 2px solid var(--frame-blue);
  }
  .card__wash {
    position: absolute;
    left: 560px;
    top: 285px;
    width: 190px;
    height: 190px;
    background: var(--wash);
    opacity: 0.6;
  }
  .owner {
    position: absolute;
    left: 40px;
    top: 160px;
    width: 318px;
    text-align: right;
    text-transform: uppercase;
    line-height: 1;
  }
  .owner__first {
    color: var(--cyan);
    font-size: 40px;
    font-weight: 400;
    letter-spacing: 1px;
  }
  .owner__last {
    color: var(--magenta);
    font-size: 50px;
    font-weight: 500;
    letter-spacing: 1px;
    margin-top: 4px;
  }
  .owner__phone {
    margin-top: 12px;
    color: var(--muted);
    font-size: 18px;
    letter-spacing: 1px;
    padding-right: 50px;
  }
  .divider {
    position: absolute;
    left: 374px;
    top: 150px;
    width: 3px;
    height: 150px;
    background: var(--ink);
  }
  .contact {
    position: absolute;
    left: 394px;
    top: 150px;
    color: var(--ink);
    font-size: 28px;
    font-weight: 400;
    line-height: 1.3;
    list-style: none;
  }
</style>
</head>
<body>
  <main class="canvas">
    <section class="card card--back" aria-label="Business card back">
      <span class="wordmark__square"></span>
      <span class="wordmark__name">Kellie-ann Drummond Salon</span>
    </section>

    <section class="card card--front" aria-label="Business card front">
      <div class="card__wash"></div>
      <div class="card__frame"></div>
      <div class="owner">
        <div class="owner__first">Kellie-ann</div>
        <div class="owner__last">Drummond</div>
        <div class="owner__phone">0482 736 219</div>
      </div>
      <div class="divider"></div>
      <ul class="contact">
        <li>Rdw@vomblet.com.au</li>
        <li>71 Willowmere Rise</li>
        <li>Corvin Cove</li>
      </ul>
    </section>
  </main>
</body>
</html>
```